Business Card Design

as above
one side to be name of business and information about business inside an imessage text bubble.
other side to be contact details around an email icon . 'envelope'

Target Market(s)

seniors

Industry/Entity Type

Business

Contact Information for Business Card

Tech Along-Keep Along
Marlene Hobb
0461 837 204
Marlene.techalong@quillmail.test
ABN:74618250913

Technology help for seniors in your own home.- tablets, music players, mobile phones, internet, email, computers. No question too small.

```html
<!DOCTYPE html>
<html lang="en">
<head>
<meta charset="utf-8">
<title>Tech Along-Keep Along – Business Cards</title>
<link rel="stylesheet" href="https://fonts.googleapis.com/css2?family=Libre+Baskerville:wght@700&family=Questrial&display=swap">
<style>
  :root {
    --page: #ecebe8;
    --card: #ffffff;
    --green: #6db85a;
    --green-deep: #4f9a3e;
    --green-soft: #b5dba8;
    --heading-green: #7cc46a;
    --ink: #4a4a4a;
    --muted: #8a8a8a;
    --orange: #ea7a2c;
  }
  * { box-sizing: border-box; margin: 0; padding: 0; }
  html, body { width: 1200px; height: 1000px; overflow: hidden; }
  body {
    background: var(--page);
    font-family: "Questrial", "Century Gothic", sans-serif;
    display: flex;
    flex-direction: column;
    align-items: center;
    justify-content: center;
    gap: 40px;
  }
  .card {
    position: relative;
    width: 800px;
    height: 457px;
    background: var(--card);
    box-shadow: 0 6px 20px rgba(0,0,0,.12);
    overflow: hidden;
  }
  .card__wave { position: absolute; inset: 0; width: 100%; height: 100%; }
  .card__title {
    position: absolute;
    font-family: "Libre Baskerville", Georgia, serif;
    font-weight: 700;
    color: var(--heading-green);
    text-transform: uppercase;
    letter-spacing: 1px;
    white-space: nowrap;
  }
  .card__name {
    position: absolute;
    font-size: 34px;
    text-transform: uppercase;
    letter-spacing: 1px;
    white-space: nowrap;
  }
  .card__name-first { color: var(--green); }
  .card__name-last { color: var(--ink); }
  .contact {
    position: absolute;
    list-style: none;
    font-size: 16px;
    color: var(--muted);
  }
  .contact__row { display: flex; align-items: center; gap: 12px; height: 26px; }
  .contact__icon { width: 16px; height: 16px; flex: none; }
  .legal {
    position: absolute;
    color: var(--orange);
    font-size: 17px;
    line-height: 1.4;
  }
  .legal__abn { display: block; }
  .services {
    position: absolute;
    color: var(--muted);
    font-size: 15px;
    line-height: 1.45;
  }
  .services__list { list-style: none; margin-top: 4px; }
  .services__list li::before {
    content: "";
    display: inline-block;
    width: 6px; height: 6px;
    border-radius: 50%;
    background: var(--green);
    margin-right: 8px;
    vertical-align: middle;
  }

  /* front */
  .card--front .card__title { left: 70px; top: 62px; font-size: 30px; }
  .card--front .card__name { left: 90px; top: 150px; }
  .card--front .contact { left: 100px; top: 238px; }
  .card--front .services { right: 40px; top: 118px; }
  .card--front .legal { left: 200px; top: 370px; }

  /* back */
  .card--back .card__title { left: 230px; top: 50px; font-size: 30px; }
  .card--back .card__name { left: 190px; top: 118px; }
  .card--back .contact { left: 200px; top: 196px; }
  .card--back .services { left: 480px; top: 230px; }
  .card--back .legal { left: 36px; top: 380px; }
</style>
</head>
<body>

<svg width="0" height="0" style="position:absolute" aria-hidden="true">
  <defs>
    <linearGradient id="band-green" x1="0" y1="0" x2="1" y2="1">
      <stop offset="0" stop-color="#5ea84b"/>
      <stop offset="1" stop-color="#a9d59b"/>
    </linearGradient>
    <symbol id="icon-phone" viewBox="0 0 16 16">
      <path d="M3.5 1.5l2.5 2.8-1.3 1.9c.9 2 2.4 3.5 4.4 4.4l1.9-1.3 2.8 2.5-1.5 2.2C7.2 13.6 2.4 8.8 1.3 3z" fill="#6db85a"/>
    </symbol>
    <symbol id="icon-mail" viewBox="0 0 16 16">
      <rect x="1" y="3" width="14" height="10" fill="#6db85a"/>
      <path d="M1 3l7 6 7-6M1 13l5-5M15 13l-5-5" fill="none" stroke="#fff" stroke-width="1.2"/>
    </symbol>
  </defs>
</svg>

<!-- Front side -->
<section class="card card--front">
  <svg class="card__wave" viewBox="0 0 800 457" preserveAspectRatio="none" aria-hidden="true">
    <path d="M0 372 C180 320 380 290 560 300 C660 306 740 330 800 345 L800 457 L0 457Z" fill="url(#band-green)"/>
    <path d="M0 356 C180 306 380 276 560 286 C660 292 740 316 800 331" fill="none" stroke="#7cc46a" stroke-width="5"/>
  </svg>
  <h1 class="card__title">Tech Along-Keep Along</h1>
  <p class="card__name"><span class="card__name-first">Marlene</span><span class="card__name-last">Hobb</span></p>
  <ul class="contact">
    <li class="contact__row"><svg class="contact__icon"><use href="#icon-phone"/></svg>0461 837 204</li>
    <li class="contact__row"><svg class="contact__icon"><use href="#icon-mail"/></svg>Marlene.techalong@quillmail.test</li>
  </ul>
  <p class="legal"><span class="legal__abn">ABN:74618250913</span>No question too small.</p>
</section>

<!-- Back side -->
<section class="card card--back">
  <svg class="card__wave" viewBox="0 0 800 457" preserveAspectRatio="none" aria-hidden="true">
    <path d="M0 300 C120 310 230 340 320 380 C400 415 460 440 520 457 L0 457Z" fill="url(#band-green)"/>
    <path d="M0 284 C120 294 240 326 330 366 C410 401 480 430 560 457" fill="none" stroke="#7cc46a" stroke-width="5"/>
  </svg>
  <h1 class="card__title">Tech Along-Keep Along</h1>
  <p class="card__name"><span class="card__name-first">Marlene</span><span class="card__name-last">Hobb</span></p>
  <ul class="contact">
    <li class="contact__row"><svg class="contact__icon"><use href="#icon-phone"/></svg>0461 837 204</li>
    <li class="contact__row"><svg class="contact__icon"><use href="#icon-mail"/></svg>Marlene.techalong@quillmail.test</li>
  </ul>
  <div class="services">
    <p>Technology help for seniors in your own home:</p>
    <ul class="services__list">
      <li>tablets</li>
      <li>music players</li>
      <li>mobile phones</li>
      <li>internet</li>
      <li>email</li>
      <li>computers</li>
    </ul>
  </div>
  <p class="legal"><span class="legal__abn">ABN:74618250913</span>No question too small.</p>
</section>

</body>
</html>
```